Kings of Polished Fog*

I am looking for a book cover which will really pop. Working title: Kings of Polished Fog (or K.P.F. for short) The concept behind the book is: education is too expensive, screwed up, and basically failing us, and even an KPF is not worth it's name anymore! How a BS is Brilliantly Stupid, a BA is great to be a Broke Artist, an MA is Mostly Antiquated and a MS Mastered Something? ...you get the point, basically I'll be ripping into a whole bunch of degree types, then walking you through what you should actually learn from an KPF. It is going to be written with a fair bit of humor, while still being fact driven. Target audience is working professionals who are considering an KPF, or have one and want a $15 refresher of all they spent $90k+ on. No color scheme is requested, Since i do like to allow creativity to flow!

Book size 5" by 8" and ebook. Author is: R.J. Halvorsen size format attached.

Went on vacation/holiday

• K.P.F. (but can be an emphasises in the Kings of Polished Fog title.
• If you look at "Lanterns over Elm Creek: a gentle account of harvest seasons on the northern farm" on brindlecart, you can see a blue/silver/white color scheme I liked in the past - but dont take that as a must by any means, the second choice was a completely different (red and white) scheme

```html
<!DOCTYPE html>
<html lang="en">
<head>
<meta charset="utf-8">
<title>Kings of Polished Fog — R.J. Halvorsen</title>
<link rel="stylesheet" href="https://fonts.googleapis.com/css2?family=Merriweather:wght@700;900&family=Open+Sans:ital,wght@0,400;1,800&display=swap">
<style>
  :root {
    --paper: #ffffff;
    --band-deep: #8a2326;
    --band-mid: #b14446;
    --title-white: #ffffff;
    --subtitle-ink: rgba(110, 18, 20, 0.55);
    --author-red: #e24448;
    --author-shadow: #a8a8a8;
    --label-ink: #222222;
  }
  html, body {
    margin: 0;
    padding: 0;
    overflow: hidden;
    background: var(--paper);
  }
  .cover {
    position: relative;
    width: 776px;
    height: 1200px;
    overflow: hidden;
    background: var(--paper);
  }
  .cover-art {
    position: absolute;
    inset: 0;
    display: block;
  }
  .torn-band {
    filter: drop-shadow(0 4px 6px rgba(0, 0, 0, 0.35));
  }
  .title-initials {
    font-family: "Merriweather", Georgia, serif;
    font-weight: 900;
    font-size: 206px;
    fill: var(--title-white);
  }
  .title-words {
    font-family: "Open Sans", Verdana, sans-serif;
    font-style: italic;
    font-weight: 800;
    font-size: 50px;
    fill: var(--subtitle-ink);
  }
  .author-name {
    position: absolute;
    left: 74px;
    top: 978px;
    margin: 0;
    font-family: "Merriweather", Georgia, serif;
    font-weight: 700;
    font-size: 50px;
    line-height: 1;
    color: var(--author-red);
    text-shadow: 2px 3px 0 var(--author-shadow);
  }
  .author-label {
    position: absolute;
    left: 75px;
    top: 1044px;
    margin: 0;
    font-family: "Open Sans", Verdana, sans-serif;
    font-weight: 400;
    font-size: 23px;
    line-height: 1;
    color: var(--label-ink);
  }
</style>
</head>
<body>
<main class="cover">
  <svg class="cover-art" width="776" height="1200" viewBox="0 0 776 1200" aria-labelledby="cover-title">
    <title id="cover-title">K.P.F. — Kings of Polished Fog</title>
    <defs>
      <linearGradient id="band-fill" x1="0" y1="0" x2="0" y2="1">
        <stop offset="0" stop-color="var(--band-deep)"/>
        <stop offset="0.45" stop-color="var(--band-mid)"/>
        <stop offset="1" stop-color="var(--band-deep)"/>
      </linearGradient>
    </defs>
    <path class="torn-band" fill="url(#band-fill)" d="
      M0,403 L28,410 L58,414 L85,411 L110,405 L135,398 L160,386 L182,371 L200,356
      L222,351 L240,344 L262,336 L290,329 L312,319 L340,316 L362,307 L385,298
      L410,281 L430,268 L450,256 L462,258 L480,273 L500,290 L530,294 L562,301
      L590,310 L620,313 L652,319 L700,322 L750,324 L762,326 L776,338
      L776,572 L762,598 L744,625 L745,643 L720,648 L700,656 L680,648 L660,640
      L645,635 L620,622 L598,623 L575,629 L557,633 L540,650 L522,664 L500,671
      L475,680 L450,688 L420,690 L395,696 L370,703 L350,704 L330,705 L298,700
      L262,694 L232,694 L200,690 L172,681 L145,677 L120,670 L98,666 L78,660
      L60,654 L35,650 L0,648 Z"/>
    <text class="title-initials" x="108" y="517" textLength="593" lengthAdjust="spacingAndGlyphs">KPF</text>
    <text class="title-words" x="145" y="558" textLength="480" lengthAdjust="spacingAndGlyphs">Kings of</text>
    <text class="title-words" x="108" y="608" textLength="572" lengthAdjust="spacingAndGlyphs">Polished Fog</text>
  </svg>
  <h2 class="author-name">R.J. Halvorsen</h2>
  <p class="author-label">Author</p>
</main>
</body>
</html>
```